Email Banner (LumenBriefs)

We require an email banner for our email promotions sent to prospect clients. The banner needs to contain the wording LumenBriefs and use the same colour scheme as the logos attached.

This is for B2B professional's so needs to look like a place you would come to read technology articles.

```html
<!DOCTYPE html>
<html lang="en">
<head>
<meta charset="utf-8">
<title>LumenBriefs Email Banner</title>
<link href="https://fonts.googleapis.com/css2?family=Montserrat:wght@600;700&display=swap" rel="stylesheet">
<style>
  :root {
    --navy: #0b1733;
    --green: #7bc043;
    --teal: #2aa39f;
    --blue: #0796d6;
    --white: #ffffff;
    --stage: #e4e6e8;
  }
  * { margin: 0; padding: 0; box-sizing: border-box; }
  html, body {
    width: 1200px;
    height: 512px;
    overflow: hidden;
    background: var(--stage);
  }
  .banner {
    position: absolute;
    left: 0;
    top: 117px;
    width: 1200px;
    height: 277px;
    background: var(--white);
    overflow: hidden;
    font-family: "Montserrat", sans-serif;
  }
  .brand-name {
    position: absolute;
    left: 52px;
    top: 54px;
    font-size: 92px;
    font-weight: 600;
    line-height: 1;
    letter-spacing: -1px;
    color: var(--navy);
  }
  .contact-band {
    position: absolute;
    left: 0;
    top: 192px;
    width: 900px;
    height: 48px;
  }
  .contact-phone,
  .contact-web {
    position: absolute;
    top: 192px;
    height: 48px;
    display: flex;
    align-items: center;
    font-weight: 700;
  }
  .contact-phone {
    left: 84px;
    font-size: 29px;
    color: var(--navy);
    gap: 10px;
  }
  .contact-web {
    left: 410px;
    font-size: 26px;
    color: var(--white);
    letter-spacing: 4px;
    gap: 12px;
  }
  .contact-icon { width: 24px; height: 24px; flex: none; }
  .growth-visual {
    position: absolute;
    right: 0;
    top: 0;
    width: 350px;
    height: 277px;
    background: linear-gradient(200deg, var(--white) 0%, #eef2f4 35%, var(--teal) 78%, var(--blue) 100%);
    clip-path: polygon(35% 0, 100% 0, 100% 100%, 0 100%);
  }
</style>
</head>
<body>
  <div class="banner">
    <div class="brand-name">LumenBriefs.io</div>

    <svg class="contact-band" viewBox="0 0 900 48" aria-hidden="true">
      <polygon points="84,0 395,0 353,48 34,48" fill="var(--green)"/>
      <polygon points="395,0 888,0 841,48 353,48" fill="var(--navy)"/>
    </svg>

    <div class="contact-phone">
      <svg class="contact-icon" viewBox="0 0 24 24" aria-hidden="true">
        <circle cx="12" cy="12" r="12" fill="var(--navy)"/>
        <path d="M8.2 6.5l2 2.2-1.1 1.5c.8 1.7 2 2.9 3.7 3.7l1.5-1.1 2.2 2-1.2 2c-4.4-.4-8.5-4.5-8.9-8.9z" fill="var(--green)"/>
      </svg>
      <span>555 0142 0199</span>
    </div>

    <div class="contact-web">
      <svg class="contact-icon" viewBox="0 0 24 24" aria-hidden="true">
        <g fill="none" stroke="var(--green)" stroke-width="1.8">
          <circle cx="12" cy="12" r="10"/>
          <ellipse cx="12" cy="12" rx="4.5" ry="10"/>
          <line x1="2" y1="12" x2="22" y2="12"/>
          <line x1="4" y1="7" x2="20" y2="7"/>
          <line x1="4" y1="17" x2="20" y2="17"/>
        </g>
      </svg>
      <span>www.lumenbriefs.io</span>
    </div>

    <div class="growth-visual" role="img" aria-label="Rising green-to-blue growth bars over a faint network of connected dots"></div>
  </div>
</body>
</html>
```